Letterhead for sustainable Last Mile Logistics needed

Dear all,

we are looking for a powerful design for our letterhead. We are a Berlin-based (Germany) logistics company which delivers parcel on the last mile in a sustainable way. Design should communicate: sustainability, integrity, one family, performance-focused, passionate for excellence and customer experience. Please find company logo attached.

Looking forward for

```html
<!DOCTYPE html>
<html lang="en">
<head>
<meta charset="utf-8">
<title>Grove Freight Letterhead</title>
<link rel="stylesheet" href="https://fonts.googleapis.com/css2?family=Open+Sans:wght@400;700&display=swap">
<style>
  :root {
    --backdrop: #cfcfcf;
    --paper: #ffffff;
    --green-deep: #1a9e4a;
    --green-fresh: #a2cd3a;
    --ink: #1d1d1d;
  }
  * { margin: 0; padding: 0; box-sizing: border-box; }
  html, body {
    width: 1200px;
    height: 686px;
    overflow: hidden;
    background: var(--backdrop);
    font-family: "Open Sans", Arial, sans-serif;
  }
  .canvas {
    position: relative;
    width: 1200px;
    height: 686px;
  }
  .letterhead {
    position: absolute;
    left: 371px;
    top: 20px;
    width: 458px;
    height: 646px;
    background: var(--paper);
    box-shadow: 0 4px 14px rgba(0,0,0,0.18);
    overflow: hidden;
  }
  .corner-shapes {
    position: absolute;
    inset: 0;
    width: 100%;
    height: 100%;
  }
  .corner-top { fill: var(--green-deep); }
  .corner-bottom { fill: var(--green-fresh); }

  .brand {
    position: absolute;
    top: 112px;
    right: 30px;
    text-align: right;
  }
  .brand-row {
    display: flex;
    align-items: center;
    justify-content: flex-end;
    gap: 7px;
  }
  .brand-dot {
    width: 16px;
    height: 16px;
    border-radius: 50%;
    background: var(--green-deep);
  }
  .brand-name {
    font-weight: 700;
    font-size: 19px;
    letter-spacing: 0.5px;
    color: var(--green-deep);
    line-height: 1;
  }
  .brand-tagline {
    margin-top: 4px;
    font-size: 9px;
    letter-spacing: 1.4px;
    color: var(--green-fresh);
  }

  .contact {
    position: absolute;
    left: 38px;
    top: 470px;
    width: 210px;
    font-size: 8.5px;
    line-height: 1.45;
    color: var(--ink);
    text-align: right;
  }
  .contact-item {
    display: flex;
    justify-content: flex-end;
    align-items: flex-start;
    gap: 6px;
  }
  .contact-item + .contact-item { margin-top: 2px; }
  .contact-icon {
    flex: none;
    width: 9px;
    height: 9px;
    margin-top: 2px;
    fill: var(--green-deep);
  }
</style>
</head>
<body>
<main class="canvas">
  <article class="letterhead">
    <svg class="corner-shapes" viewBox="0 0 458 646" preserveAspectRatio="none" aria-hidden="true">
      <path class="corner-top" d="M292 0 H458 V104 Q418 28 292 0 Z"/>
      <path class="corner-bottom" d="M0 548 Q62 628 198 646 H0 Z"/>
    </svg>

    <header class="brand">
      <div class="brand-row">
        <span class="brand-dot"></span>
        <span class="brand-name">GROVE FREIGHT</span>
      </div>
      <p class="brand-tagline">SUSTAINABLE LAST MILE</p>
    </header>

    <footer class="contact">
      <div class="contact-item">
        <span>Northfield 18 Works, 52 Linden Park Road<br>Suite #210; Riverton, OR,<br>USA Zip Code: 97410</span>
        <svg class="contact-icon" viewBox="0 0 10 10" aria-hidden="true"><path d="M5 0a3.5 3.5 0 0 0-3.5 3.5C1.5 6 5 10 5 10s3.5-4 3.5-6.5A3.5 3.5 0 0 0 5 0zm0 5a1.5 1.5 0 1 1 0-3 1.5 1.5 0 0 1 0 3z"/></svg>
      </div>
      <div class="contact-item">
        <span>(555) 014-2738</span>
        <svg class="contact-icon" viewBox="0 0 10 10" aria-hidden="true"><path d="M2 0.5l1.8 2.2-1 1.1c.6 1.4 1.7 2.5 3.1 3.1l1.1-1L9.5 7.7 8.3 9.5C4.1 9.2.8 5.9.5 1.7z"/></svg>
      </div>
      <div class="contact-item">
        <span>www.grovefreight.example</span>
        <svg class="contact-icon" viewBox="0 0 10 10" aria-hidden="true"><path d="M5 0a5 5 0 1 0 0 10A5 5 0 0 0 5 0zm0 1c.6.7 1 1.8 1.1 3.5H3.9C4 2.8 4.4 1.7 5 1zM1.1 5.5h1.8c.1 1.3.4 2.4.9 3.2A4 4 0 0 1 1.1 5.5zm0-1A4 4 0 0 1 3.8 1.3c-.5.8-.8 1.9-.9 3.2zM5 9c-.6-.7-1-1.8-1.1-3.5h2.2C6 7.2 5.6 8.3 5 9zm1.2-.3c.5-.8.8-1.9.9-3.2h1.8a4 4 0 0 1-2.7 3.2zm.9-4.2c-.1-1.3-.4-2.4-.9-3.2a4 4 0 0 1 2.7 3.2z"/></svg>
      </div>
      <div class="contact-item">
        <span>hello@grovefreight.example</span>
        <svg class="contact-icon" viewBox="0 0 10 10" aria-hidden="true"><path d="M0 2h10v6H0zm1 1v.3L5 6l4-2.7V3z"/></svg>
      </div>
    </footer>
  </article>
</main>
</body>
</html>
```